CorkGlow Artbook for Okanagan Region, British Columbia

Creating an art book: CorkGlow, for the Okanagan Wine Region in British Columbia, Canada. Would like smart, modern, clean and linear...cool, sexy urban, not ugly boring suburban... I need a cover that appeals to the wino in all of us! Title: CorkGlow -Marla Pendrick
Updates
Thank you all kindly for your efforts. I have added some files so that you can get a sense of my aesthetic...it's never easy trying to figure it out, is it? I will hopefully have dimensions of book soon...cheers, Marla
would anyone please design a giant wine bottle with the wine label that looks like a label but says corkglow...just curious to see if it works as a design or not...thank you.
Target Market(s)
Designing this wine art book of quotes to wineries in Okanagan BC. Buyer is wine lover and tourist ready to spend his vacation bucks on this wonderful book!
Look and feel

```html
<!DOCTYPE html>
<html lang="en">
<head>
<meta charset="utf-8">
<title>CorkGlow — Cover</title>
<link href="https://fonts.googleapis.com/css2?family=Oleo+Script:wght@700&display=swap" rel="stylesheet">
<style>
  :root {
    --sky-light: #e6e6e6;
    --sky-dark: #cdcdcd;
    --band: #4f4f4f;
    --wine-bright: #f20f00;
    --wine-deep: #cf2b04;
    --ink-light: #ffffff;
  }
  html, body {
    margin: 0;
    padding: 0;
    overflow: hidden;
    background: #ffffff;
  }
  .cover {
    position: relative;
    width: 928px;
    height: 1200px;
    overflow: hidden;
    font-family: "Oleo Script", cursive;
  }
  .cover__sky {
    position: absolute;
    left: 0; top: 0;
    width: 100%;
    height: 346px;
    background: radial-gradient(ellipse at 50% 0%, var(--sky-light) 0%, var(--sky-dark) 100%);
  }
  .cover__title-band {
    position: absolute;
    left: 0; top: 346px;
    width: 100%;
    height: 167px;
    background: var(--band);
    display: flex;
    align-items: center;
    justify-content: center;
  }
  .cover__title {
    margin: 0;
    color: var(--ink-light);
    font-size: 120px;
    font-weight: 700;
    font-style: italic;
    line-height: 1;
    letter-spacing: 1px;
    transform: translateY(6px);
  }
  .cover__field {
    position: absolute;
    left: 0; top: 513px;
    width: 100%;
    height: 687px;
    background: radial-gradient(ellipse at 50% 0%, var(--wine-bright) 0%, var(--wine-deep) 100%);
  }
  .cover__glass {
    position: absolute;
    left: 673px; top: 713px;
    width: 162px;
    height: 383px;
    border-radius: 10px;
    background: linear-gradient(180deg, rgba(255,255,255,0.14) 0%, rgba(255,255,255,0.06) 100%);
  }
  .cover__author {
    position: absolute;
    right: 35px;
    top: 1124px;
    margin: 0;
    color: var(--ink-light);
    font-size: 31px;
    font-weight: 700;
    font-style: italic;
    line-height: 1;
    letter-spacing: 0.5px;
  }
</style>
</head>
<body>
  <main class="cover">
    <div class="cover__sky"></div>
    <header class="cover__title-band">
      <h1 class="cover__title">CorkGlow</h1>
    </header>
    <section class="cover__field">
    </section>
    <div class="cover__glass" role="img" aria-label="White line drawing of a wine glass, partly filled"></div>
    <p class="cover__author">by Marla Pendrick</p>
  </main>
</body>
</html>
```